Awesome Digital Ad Design – Quorvex Remarketing

I am going to be setting up a Quorvex Remarketing ad campaign I need creatives for.

Several sizes are needed in the end, however, please submit your design concept in the following 2 sizes to start:
Medium rectangle: 300X250
Leaderboard: 728X90

Original artwork/design files and images used expected upon payment and as part of the final delivery.

Ads should match our company brand and the information on this webpage: http://www.brightlanesystems.com/real-estate-marketing/
SEE MORE INSTRUCTIONS IN ATTACHED WORD DOC
Updates

Project Deadline Extended Reason: Extending deadline to designers hoping to receive more design concept options. Thanks to everyone who has already submitted! Added Wednesday, February 8, 2017

Target Market(s)

Business-To-Business Audience –Real Estate Company Executives (Presidents/VPs/Owners/CEOs/Sales Managers).

Industry/Entity Type

Real Estate

Font styles to use
Sans Serif

Requirements
Must have
• Copy should be minimal words, billboard like. Please use real photos/images that would appeal to real estate high-level decision-maker executives.
Should not have
• No cartoons or graphics

```html
<!DOCTYPE html>
<html lang="en">
<head>
<meta charset="UTF-8">
<title>Brightlane Systems – Leaderboard Ad</title>
<link href="https://fonts.googleapis.com/css2?family=Roboto+Condensed:wght@400;700&display=swap" rel="stylesheet">
<style>
  :root {
    --maroon: #6d2a35;
    --maroon-deep: #5e222c;
    --gold: #c9b47c;
    --button-gold: #8f7b3b;
    --white: #ffffff;
    --ink: #2b2b2b;
    --photo-light: #7fb3d6;
    --photo-mid: #3f78a8;
    --photo-dark: #1b3452;
  }
  * { margin: 0; padding: 0; box-sizing: border-box; }
  html, body { width: 1200px; height: 148px; overflow: hidden; background: var(--white); }
  .ad {
    position: relative;
    width: 1200px;
    height: 148px;
    background: linear-gradient(90deg, var(--maroon) 0%, var(--maroon-deep) 100%);
    font-family: "Roboto Condensed", Arial, sans-serif;
    overflow: hidden;
  }
  .brand-panel {
    position: absolute;
    left: 0; top: 0;
    width: 178px; height: 148px;
    background: var(--white);
    display: flex;
    align-items: center;
    justify-content: center;
    gap: 8px;
  }
  .brand-dot {
    width: 12px; height: 12px;
    border-radius: 50%;
    background: var(--maroon);
    flex: none;
  }
  .brand-name {
    color: var(--ink);
    font-weight: 400;
    font-size: 21px;
    line-height: 1.05;
  }
  .headline {
    position: absolute;
    left: 198px; top: 18px;
    width: 420px;
    text-align: center;
    font-weight: 700;
    font-size: 29px;
    color: var(--white);
    letter-spacing: 0.2px;
    white-space: nowrap;
  }
  .headline .accent { color: var(--gold); }
  .divider {
    position: absolute;
    left: 198px; top: 70px;
    width: 412px; height: 1px;
    background: var(--gold);
    opacity: 0.7;
  }
  .offer {
    position: absolute;
    left: 198px; top: 82px;
    width: 420px;
    text-align: center;
    font-weight: 400;
    font-size: 23px;
    line-height: 29px;
    color: var(--white);
  }
  .photo {
    position: absolute;
    left: 610px; top: 0;
    width: 380px; height: 148px;
  }
  .cta-arrow {
    position: absolute;
    left: 1003px; top: 62px;
  }
  .cta-button {
    position: absolute;
    left: 1023px; top: 53px;
    width: 142px; height: 42px;
    background: var(--button-gold);
    color: var(--white);
    font-weight: 700;
    font-size: 19px;
    display: flex;
    align-items: center;
    justify-content: center;
    text-decoration: none;
    letter-spacing: 0.3px;
  }
</style>
</head>
<body>
  <div class="ad">
    <div class="brand-panel">
      <span class="brand-dot"></span>
      <span class="brand-name">Brightlane<br>Systems</span>
    </div>

    <h1 class="headline">CLIENT FOLLOW-UP <span class="accent">MADE SIMPLE</span></h1>
    <div class="divider"></div>
    <p class="offer">VIRTUALLY NO COST TO<br>YOUR COMPANY!</p>

    <svg class="photo" width="380" height="148" viewBox="0 0 380 148" role="img" aria-label="Photo of business executives shaking hands in a glass office overlooking a city skyline">
      <defs>
        <linearGradient id="photoTone" x1="0" y1="0" x2="1" y2="1">
          <stop offset="0" stop-color="var(--photo-light)"/>
          <stop offset="0.5" stop-color="var(--photo-mid)"/>
          <stop offset="1" stop-color="var(--photo-dark)"/>
        </linearGradient>
      </defs>
      <path d="M 40 0 Q -10 74 40 148 L 380 148 L 380 0 Z" fill="url(#photoTone)"/>
    </svg>

    <svg class="cta-arrow" width="18" height="24" viewBox="0 0 18 24" aria-hidden="true">
      <polygon points="0,0 18,12 0,24" fill="var(--white)"/>
    </svg>
    <a class="cta-button" href="#">LEARN MORE</a>
  </div>
</body>
</html>
```